New Innovative Counselling and psychotherapy Service needs Business Card design

Keep it simple and professional. On one side, just company name and logo (perhaps in all blue) and maybe a tag line.

On other side (all white) my name and Qualifications in centre

Industry/Entity Type

Health And Wellness

Contact Information for Business Card

Derek Hollis
Counsellor & Psychotherapist
BSc (Psychol.), BA, Dip. (Couns. & Psych.), PG.Cert (CBT), MGVrA, NWTF

I will also require Mobile no, Email and web site address of which I'll pass on to final designer.

Font styles to use
Sans Serif

Requirements
Must have
• My Logo Only and please use the colours in logo that is in it.
Should not have
• Any other images

```html
<!DOCTYPE html>
<html lang="en">
<head>
<meta charset="utf-8">
<title>Brightpath Lane – Business Card</title>
<link rel="stylesheet" href="https://fonts.googleapis.com/css2?family=Roboto:wght@400;500&family=Roboto+Condensed:wght@400;700&display=swap">
<style>
  :root {
    --backdrop: #2e2e2e;
    --card-white: #f1f1f1;
    --brand-blue: #46b3ec;
    --brand-green: #97d45b;
    --ink: #3a3a3a;
    --text-light: #ffffff;
  }
  * { margin: 0; padding: 0; box-sizing: border-box; }
  html, body {
    width: 1200px; height: 960px; overflow: hidden;
    background: var(--backdrop);
    font-family: "Roboto", Arial, sans-serif;
  }
  .canvas { position: relative; width: 1200px; height: 960px; }

  .card {
    position: absolute;
    width: 600px; height: 342px;
    box-shadow: 0 4px 10px rgba(0,0,0,0.45);
    overflow: hidden;
  }
  .card--front { left: 322px; top: 110px; background: var(--card-white); }
  .card--back { left: 320px; top: 493px; background: var(--brand-blue); }

  .brand {
    position: absolute; left: 132px; top: 84px;
    display: flex; align-items: center; gap: 24px;
  }
  .brand__dot {
    width: 62px; height: 62px; border-radius: 50%;
    background: var(--brand-blue);
  }
  .brand__name {
    font-size: 32px; font-weight: 400; color: var(--ink);
    letter-spacing: 0.2px;
  }

  .info-band {
    position: absolute; left: 0; top: 235px; width: 100%; height: 107px;
    display: flex; gap: 3px; background: #ffffff;
  }
  .info-band__person {
    width: 316px; background: var(--brand-blue); color: var(--text-light);
    padding: 16px 0 0 27px;
    font-family: "Roboto Condensed", Arial, sans-serif;
  }
  .person__name { font-size: 21px; font-weight: 700; line-height: 22px; }
  .person__role { font-size: 14px; font-weight: 700; margin-top: 4px; line-height: 16px; }
  .person__quals { font-size: 11.5px; font-weight: 400; margin-top: 3px; line-height: 14px; }

  .info-band__contact {
    flex: 1; background: var(--brand-green); color: var(--text-light);
    padding: 22px 24px 0 0;
    display: flex; flex-direction: column; align-items: flex-end; gap: 2px;
  }
  .contact__line {
    display: flex; align-items: center; gap: 7px;
    font-size: 14px; line-height: 17px;
  }
  .contact__icon { width: 12px; height: 12px; fill: var(--text-light); }

  .back__mark {
    position: absolute; left: 240px; top: 70px;
    width: 120px; height: 120px; border-radius: 50%;
    background: #ffffff;
  }
  .back__name {
    position: absolute; left: 0; top: 206px; width: 100%;
    text-align: center; color: var(--text-light);
    font-size: 26px; font-weight: 400;
  }
  .back__tagline {
    position: absolute; left: 0; top: 288px; width: 100%;
    text-align: center; color: var(--text-light);
    font-size: 14px; font-weight: 400;
  }
</style>
</head>
<body>
<main class="canvas">
  <section class="card card--front">
    <div class="brand">
      <span class="brand__dot"></span>
      <span class="brand__name">Brightpath Lane</span>
    </div>
    <div class="info-band">
      <div class="info-band__person">
        <p class="person__name">DEREK HOLLIS</p>
        <p class="person__role">COUNSELLOR &amp; PSYCHOTHERAPIST</p>
        <p class="person__quals">BSc (Psychol.), BA, Dip. (Couns. &amp; Psych.)<br>PG.Cert (CBT), MGVrA,</p>
      </div>
      <div class="info-band__contact">
        <p class="contact__line">555 012 3478
          <svg class="contact__icon" viewBox="0 0 12 12"><path d="M3 0h6a1 1 0 0 1 1 1v10a1 1 0 0 1-1 1H3a1 1 0 0 1-1-1V1a1 1 0 0 1 1-1zm0.5 1.5v7.5h5V1.5z"/></svg>
        </p>
        <p class="contact__line">derek@Brightpathlane.com
          <svg class="contact__icon" viewBox="0 0 12 12"><path d="M0 2.5h12v7H0z M0.5 2.8l5.5 4 5.5-4" stroke="#97d45b" stroke-width="0.9"/></svg>
        </p>
        <p class="contact__line">www.Brightpathlane.com
          <svg class="contact__icon" viewBox="0 0 12 12"><circle cx="6" cy="6" r="5.5"/><path d="M2.5 4c1.5 0 2 1 3 .5s.5 2 1.5 2.5-1 2.5-1 3.5M8 1.5c-.5 1 .5 1.5 1.5 1.5" stroke="#97d45b" stroke-width="1" fill="none"/></svg>
        </p>
      </div>
    </div>
  </section>

  <section class="card card--back">
    <span class="back__mark"></span>
    <p class="back__name">Brightpath Lane</p>
    <p class="back__tagline">Caring For Your Psychological Well-Being Is Our Top Priority</p>
  </section>
</main>
</body>
</html>
```